Flyer für kleine christliche Gemeinde
professionelles Vorgehen. pulvrin hat sehr gut Sinn und Konzept unserer Veranstaltung erfasst und den Flyer mit passenden Bildern und angemessener Designgestaltung versehen. Stach aus den anderen Vorschlägen heraus. Änderungswünsche und auch Planänderungen unsererseits wurden geduldig und sehr geschmackvoll umgesetzt. Wer ein fundiertes, modernes und ansprechendes, passendes Design braucht ist mit diesem Designer gut beraten.
Zielgruppe
kleine christliche Gemeinde, Einladung zu einer Vortragsreihe zu aktuellen Themen /Krisen unserer Zeit, Zielgruppe: Erwachse Menschen aller Couleur mit Interesse an aktuellem Zeitgeschehen und Antworten für die Probleme unserer Zeit, Sinn- und Orientierungssuchende, Bibelinteressierte
Aufgabenstellung
Aufmerksamkeit fesselnder, dennoch seriös wirkender, informativer Flyer als Einladung zu einer Vortragsreihe, Verteilung per Hand auf der Straße und in Briefkästen, Information zum Redner kürzen wenn nötig, Anfahrtsskizze und Informationen zu Erreichbarkeit (Bus...), Stockbilder möglichst kostenfreie verwenden,

```html
<!DOCTYPE html>
<html lang="de">
<head>
<meta charset="utf-8">
<title>Flyer – Evangelisation mit Markus</title>
<link rel="stylesheet" href="https://fonts.googleapis.com/css2?family=Oswald:wght@400;500;600&family=Raleway:ital,wght@0,300;0,400;0,500;0,600;0,800;1,400&family=Archivo+Narrow:ital,wght@0,400;1,400&display=swap">
<style>
:root{
  --bg:#c9c9c9;
  --paper:#ffffff;
  --blush:#f2dfdc;
  --sky:#6aaadc;
  --magenta:#e3236a;
  --ink:#1c1c1c;
  --rule:#e6c9c5;
}
*{margin:0;padding:0;box-sizing:border-box}
html,body{width:710px;height:1200px;overflow:hidden;background:var(--bg)}
body{position:relative;font-family:"Raleway",sans-serif;color:var(--ink)}
.spread{position:absolute;left:10px;width:690px;height:532px;background:var(--paper);overflow:hidden}
.spread--outer{top:40px}
.spread--inner{top:610px}
.abs{position:absolute}

/* outer: back page */
.back-band{left:0;top:0;width:284px;height:415px;background:var(--sky)}
.back-edge{left:0;top:137px;width:7px;height:278px;background:var(--blush)}
.back-rule{left:102px;top:254px;width:243px;height:1px;background:var(--rule)}
.map-frame{background:var(--paper)}
.map-top{left:102px;top:25px;width:182px;height:116px;padding:8px 7px 12px 7px}
.map-fill{width:100%;height:100%;background:linear-gradient(135deg,#eef0f3 0%,#dfe4ea 45%,#a9c6e6 60%,#eceef1 100%)}
.map-bottom{left:179px;top:338px;width:132px;height:163px;background:linear-gradient(160deg,#eef0f3 0%,#e3e7ec 40%,#9fd6e8 55%,#e9ebee 70%,#d7dce3 100%)}
.info-label{font-family:"Oswald",sans-serif;font-weight:600;font-size:10px;letter-spacing:.12em;color:var(--ink)}
.info-line{font-size:8.6px;color:var(--ink);white-space:nowrap}

/* outer: title page */
.front{left:345px;top:0;width:345px;height:532px;background:var(--blush)}
.entry-note{left:189px;top:31px;width:135px;height:36px;background:linear-gradient(90deg,rgba(227,35,106,.18),rgba(227,35,106,.32))}
.cover-photo{left:84px;top:152px;width:212px;height:310px;background:linear-gradient(180deg,#b9d3ec 0%,#e9e2c2 30%,#f3c531 55%,#d9a81e 70%,#5b8a3a 100%)}
.cover-title{left:35px;top:74px;font-family:"Oswald",sans-serif;font-weight:500;font-size:54px;line-height:53px;letter-spacing:.1em;color:var(--magenta);white-space:nowrap}
.edge-bar{width:7px;height:257px;background:var(--sky)}
.front .edge-bar{left:338px;top:137px}
.kicker{left:70px;top:505px;transform:rotate(-90deg);transform-origin:left top;font-family:"Oswald",sans-serif;font-weight:500;font-size:7px;letter-spacing:.06em;white-space:nowrap}
.sub-rule{left:84px;top:471px;width:93px;height:4px;background:var(--sky)}
.subline{left:84px;top:483px;font-size:8.6px;line-height:10.5px;color:var(--ink)}

/* inner spread */
.series-head{left:30px;top:27px;color:var(--sky);font-weight:800;line-height:1}
.series-head .s1{font-size:28px;display:block;margin-bottom:9px}
.series-head .s2{font-size:28px;display:block;margin-bottom:6px}
.series-head .s3{font-size:36px;display:block;margin-bottom:4px;letter-spacing:-.01em}
.series-head .s4{font-size:22.5px;display:block;white-space:nowrap}
.inner-left-bar{left:0;top:137px}
.topics{left:31px;top:176px;width:264px;font-size:12px;line-height:15px;font-weight:300;color:var(--magenta)}
.col{font-family:"Archivo Narrow",sans-serif;font-size:8.2px;line-height:9.6px;color:var(--ink)}
.col p{margin-bottom:6px}
.col-a{left:31px;top:271px;width:124px}
.col-b{left:168px;top:272px;width:128px}
.verse-head{font-family:"Raleway",sans-serif;font-weight:800;color:var(--sky);font-size:12.5px;line-height:12px;margin-bottom:7px}
.verse-head small{font-size:10px}
.pink-panel{left:319px;top:30px;width:285px;height:374px;background:var(--blush)}
.intro-rule{left:324px;top:35px;width:58px;height:4px;background:var(--sky)}
.intro{left:387px;top:32px;width:128px;font-size:7.6px;line-height:12.2px;font-weight:600}
.program{left:530px;top:32px;width:150px;font-size:7.6px;line-height:8.6px}
.program .talk{font-weight:500;color:var(--ink)}
.program .when{color:var(--sky);margin:4px 0 7px}
.inner-photo{left:444px;top:229px;width:237px;height:158px;background:linear-gradient(160deg,#cfe0f2 0%,#f1f3f6 30%,#e8583a 45%,#d93a2a 55%,#f1c83a 80%,#f6e7a8 100%)}
.inner-right-bar{left:683px;top:137px;height:259px}
.speaker-head{left:353px;top:355px;font-weight:800;font-size:31px;line-height:32px;color:var(--sky)}
.bio{left:353px;top:428px;width:308px;font-family:"Archivo Narrow",sans-serif;font-style:italic;font-size:7.3px;line-height:9.5px;color:#333}
</style>
</head>
<body>

<section class="spread spread--outer">
  <div class="abs back-band"></div>
  <div class="abs back-edge"></div>
  <div class="abs back-rule"></div>
  <div class="abs map-frame map-top"><div class="map-fill" role="img" aria-label="Lageplan mit Zugängen zum Veranstaltungsort"></div></div>

  <div class="abs info-label" style="left:102px;top:148px">VERANSTALTUNG</div>
  <div class="abs info-line" style="left:102px;top:173px">Kulturzentrum Lindenhof-Haus</div>
  <div class="abs info-line" style="left:102px;top:190px">Lindenallee 1</div>
  <div class="abs info-line" style="left:102px;top:207px">16500 Birkenfeld</div>
  <div class="abs info-line" style="left:102px;top:224px">Nähe Schloß Birkenfeld</div>

  <div class="abs info-label" style="left:102px;top:257px">E-MAIL</div>
  <div class="abs info-line" style="left:103px;top:282px">IhreInfo@website.de</div>
  <div class="abs info-label" style="left:102px;top:309px">TELEFON</div>
  <div class="abs info-line" style="left:103px;top:334px">+01 234 567 890</div>
  <div class="abs info-label" style="left:102px;top:361px">ADRESSE</div>
  <div class="abs info-line" style="left:103px;top:386px">Straße 123</div>
  <div class="abs info-line" style="left:103px;top:402px">45678 Stadt</div>

  <div class="abs map-bottom" role="img" aria-label="Anfahrtsskizze mit Fußweg von der Bushaltestelle"></div>

  <div class="abs front">
    <div class="abs entry-note" role="img" aria-label="Handschriftlicher Hinweis: Eintritt frei"></div>
    <div class="abs cover-photo" role="img" aria-label="Foto: gelbe Tulpen unter einem Wasserstrahl vor blauem Himmel"></div>
    <h1 class="abs cover-title">Evangeli-<br>sation mit<br>Markus</h1>
    <div class="abs edge-bar"></div>
    <div class="abs kicker">Warnrufe unserer Zeit</div>
    <div class="abs sub-rule"></div>
    <p class="abs subline">oder wie wir unsere Freiheit/Individualität<br>verkaufen/- verspielen</p>
  </div>
</section>

<section class="spread spread--inner">
  <h2 class="abs series-head">
    <span class="s1">Eine</span>
    <span class="s2">Kurz-Serie mit</span>
    <span class="s3">Markus Feld</span>
    <span class="s4">Frühling, 8.–11. Mai 2025</span>
  </h2>
  <div class="abs edge-bar inner-left-bar"></div>
  <p class="abs topics">1) The Way Out Of Fear; 2) Voices Of Warning; 3) Freedom Or Control. As you can see, each one of those topics can take us more than one presentation</p>

  <div class="abs col col-a">
    <div class="verse-head">Die Bibel, <small>Lukas Kapitel 21, Vers 25-26</small><br><small>[Übersetzung nach Neue Lesebibel]</small></div>
    <p>Bedrohungen durch Krieg, Umwelt&shy;katastrophen, Klimawandel, zunehmende soziale Unsicherheit/ Ungerechtigkeit und Zerfall/ Spaltung der Gesellschaft erfüllen uns immer mehr mit Sorgen für die Zukunft.</p>
    <p>Politiker und die Mächtigen der Welt suchen in Weltwirtschaftsforen und Klimakonferenzen nach Antworten und Lösungswegen globaler Probleme. Wirtschaft, Wissenschaft, Politik und Kirchen suchen nach Orientierung und Führung, geradezu nach einem Erlöser, der die Kräfte für den</p>
  </div>
  <div class="abs col col-b">
    <p>Rettungsweg unseres Planeten eint.</p>
    <p>Fakenews im Netz, Verschwörungstheorien, aufsehen&shy;erregende Berichterstattung und voreilige politische Planspiele steigern die Verunsichern der Menschen. Die tatsächliche Ratlosigkeit der Großen und Mächtigen und die Verunsicherung der Bevölkerung der Welt spiegeln sich dramatisch in folgenden Worten wieder:</p>
    <p>“Und es werden Zeichen geschehen an Sonne und Mond und Sternen, und auf Erden Angst der Völker vor Ratlosigkeit bei dem Tosen des Meeres und der Wogen, da die Menschen vor Furcht und Ohnmacht sinken werden vor Furcht und Erwartung dessen, was über den Erdkreis kommen soll; denn die Kräfte des Himmels werden erschüttert werden.”</p>
  </div>

  <div class="abs pink-panel"></div>
  <div class="abs intro-rule"></div>
  <p class="abs intro">Doch wo stehen wir? Wie kommen wir durch die Wirrnisse dieser Zeit? Welche echten Lösungsansätze gibt es? Erfahren Sie Gottes Fahrplan für diese Welt. Lernen Sie den einzigen Ausweg und die Chance kennen, Ihre persönliche Individualität und einen kühlen Kopf zu bewahren und finden echte Sicherheit auf ihrem Weg in/durch unsicheren Zeiten.</p>

  <div class="abs program">
    <div class="talk">1) Ein Weg aus der Angst</div>
    <div class="when">Echte Freiheit und<br>Unabhängigkeit<br>(Do., 8.5., 18:30 Uhr)</div>
    <div class="talk">2) Stimmen der Warnung</div>
    <div class="when">Systeme der Macht - der<br>Kampf um unseren Kopf<br>(Fr., 9.5., 18:30 Uhr)</div>
    <div class="talk">3) Freiheit oder Kontrolle –<br>wem folgen wir?</div>
    <div class="when">Erzwungene/Erpresste<br>Loyalität - wie wir sie zeigen<br>müssen (Sa., 10.5., 18:30 Uhr)</div>
    <div class="talk">4) ??????????????????????</div>
    <div class="when">????????????????????<br>(So., 11.5., 18:30 Uhr)</div>
  </div>

  <div class="abs inner-photo" role="img" aria-label="Foto: rote und gelbe Tulpen vor blühendem Baum"></div>
  <div class="abs edge-bar inner-right-bar"></div>
  <h3 class="abs speaker-head">Zum<br>Sprecher</h3>
  <p class="abs bio">Pfarrer Markus Feld wurde in San Marcos, Costa Serena, geboren. In seinen früheren Jahren besuchte er das katholische Priesterseminar San Lucas in der Hoffnung, Priester zu werden. Während eines Besuchs in den Vereinigten Staaten wurde er zu einem Seminar über Prophezeiungen in Daniel und der Offenbarung in Port Avalon, Nordküste, eingeladen. Nachdem er die Zuverlässigkeit der biblischen Prophetien erkannt hatte, ließ er sich taufen und schloss sein Pastorenstudium an der Theologischen Hochschule Karibik in Bahía Clara ab. Er ist Pastor der Gemeinde Lebendiges Wort, Herausgeber des Morgenbote und moderiert wöchentliche Radiosendungen.</p>
</section>

</body>
</html>
```